Harbor & Quillstone executive recruiting services

I started a plankfold website using an existing template and some of the original content is still on this UNpublished work in progress. I am an executive recruiter offering services to both Clients and Candidates in many sectors and using creative sourcing methodologies. I have 30+ years of business experience combined with my recruiting experience. I like the color teal and used it for the site I started. The tabs should be
About (me)
Services (for Clients and Candidates)
Industry Coverage
Recruiting Process (see attached flow chart)
Retained Agreement (see attached)
Personal Commitment
Testimonials
Content/articles/blogs etc
Contact
Updates

TO ALL DESIGNERS:
I have been granted a short extension to choose a design. Please resubmit designs using a new name DROVE EXECUTIVE SEARCH. Pls feel free to alert me with any questions and of course, when the edits are made.

thank you

Colette

Target Market(s)

Executives from Director, VP, SVP and C-Suite

Industry/Entity Type

recruiting industry for finance, Human Resoures, Sales/Marketing, Innovation/Transformation , Information Technology, Entertainment/Media/Telecommunications, Healthcare/Life Sciences,HCIT/Biotech

Font styles to use
Sans Serif

Colors
0094D4
00A9DD
6FCCEA
C7EBF8
E9F6FB

Requirements
Must have
• way to contact me - add calendar sign up
Nice to have
• process flow for the recruiting process (see attached)
Should not have
• guarantees

```html
<!DOCTYPE html>
<html lang="en">
<head>
<meta charset="utf-8">
<title>Drove Executive Search</title>
<link href="https://fonts.googleapis.com/css2?family=Ubuntu:wght@400;500;700&family=Roboto:wght@400;500&display=swap" rel="stylesheet">
<style>
:root{
  --blue:#0094D4;
  --sky:#00A9DD;
  --aqua:#6FCCEA;
  --ice:#C7EBF8;
  --mist:#E9F6FB;
  --ink:#222;
  --dark:#1f1f21;
  --grey:#c3c3c3;
}
*{box-sizing:border-box;margin:0;padding:0}
html,body{width:1200px;height:4508px;overflow:hidden}
body{font-family:"Roboto",sans-serif;color:var(--ink);background:#fff;font-size:14px;line-height:26px}
a{color:inherit;text-decoration:none}
.wrap{width:976px;margin:0 auto;position:relative}

/* header */
.site-header{background:var(--dark);height:135px;color:#fff}
.site-header .top{height:80px;display:flex;align-items:center;justify-content:space-between;border-bottom:1px solid #3a3a3c}
.brand{font-family:"Ubuntu",sans-serif;font-weight:500;font-size:25px;letter-spacing:.3px}
.btn-solid{background:var(--sky);color:#fff;border-radius:22px;padding:0 34px;height:41px;line-height:41px;font-size:14px;font-weight:500}
.nav{display:flex;justify-content:space-between;padding:0 6px;font-size:14px;height:55px;align-items:center;color:#e5e5e5}

/* hero */
.hero{height:455px;background:linear-gradient(135deg,#0c4f85 0%,#1d7fc0 35%,#3aa6df 60%,#0f5e9c 100%);color:#fff;text-align:center;position:relative}
.hero .inner{position:absolute;inset:0;background:rgba(0,70,130,.25)}
.hero .welcome{position:absolute;top:125px;left:0;right:0;font-family:"Ubuntu",sans-serif;font-size:42px;font-weight:500}
.hero h1{position:absolute;top:178px;left:0;right:0;font-family:"Ubuntu",sans-serif;font-size:58px;font-weight:500;letter-spacing:.5px}
.btn-ghost{display:inline-block;border:2px solid #fff;border-radius:24px;color:#fff;height:45px;line-height:41px;padding:0 34px;font-size:14px;font-weight:500}
.hero .btn-ghost{position:absolute;top:270px;left:522px}

/* about */
.about{height:447px;padding-top:92px}
.about .wrap{display:flex}
.about-title{width:339px;font-family:"Ubuntu",sans-serif}
.about-title .kicker{font-size:26px;font-weight:500;color:var(--ink)}
.about-title .big{font-size:36px;line-height:50px;color:var(--sky);font-weight:500;margin-top:14px}
.about-text{width:637px;font-size:14px;line-height:26px;text-align:justify}
.about-text p{margin-bottom:11px}

/* audience */
.audience{height:437px;background:linear-gradient(115deg,#0a6fb4 0%,#1487cd 45%,#0a8fd0 46%,#1aa6e0 75%,#0d93d6 100%);color:#fff;padding-top:40px}
.audience .wrap{display:flex;justify-content:space-between}
.audience .col{width:436px;text-align:justify;font-size:14px;line-height:26px}
.audience h2{font-family:"Ubuntu",sans-serif;font-size:29px;font-weight:500;margin-bottom:22px;text-align:left}
.audience p{margin-bottom:16px}

/* more about */
.more{height:931px;padding-top:60px;position:relative}
.section-title{font-family:"Ubuntu",sans-serif;font-size:33px;font-weight:500;color:var(--sky);text-align:center}
.more .cols{display:flex;justify-content:space-between;margin-top:42px}
.more .col{width:473px;text-align:justify}
.more .col p{margin-bottom:9px}
.more .accent{color:var(--blue)}
.photo{position:absolute}
.photo-meeting{left:112px;top:419px;width:457px;height:287px;background:linear-gradient(135deg,#c9a78b,#8a6a54 45%,#d9d4cf);box-shadow:0 4px 10px rgba(0,0,0,.15)}
.photo-team{left:523px;top:537px;width:565px;height:259px;background:linear-gradient(135deg,#6f5a4e,#2e3a4e 50%,#c9b8a8);border-top:3px solid #fff;border-left:3px solid #fff}

/* process */
.process{height:724px;position:relative}
.process .section-title{position:absolute;top:-22px;left:0;right:0}
.process .sub{position:absolute;top:36px;left:0;right:0;text-align:center;font-size:14px}
.step{position:absolute;width:170px;text-align:center;font-size:14px;line-height:24px}
.step .num{font-family:"Ubuntu",sans-serif;font-size:25px;font-weight:500;color:var(--blue);line-height:34px}
.tile{position:absolute;width:82px;height:70px;border-radius:5px;background:linear-gradient(160deg,#1fb4ea,#0b7fc6);box-shadow:2px 3px 5px rgba(0,0,0,.3);display:flex;align-items:center;justify-content:center}
.tile svg{width:40px;height:40px;fill:none;stroke:#fff;stroke-width:1.8;stroke-linecap:round;stroke-linejoin:round}
.process .note{position:absolute;top:585px;left:112px;width:976px;text-align:center;font-size:14px;line-height:26px}

/* commitment */
.commit{position:relative;height:437px}
.panel{position:absolute;left:112px;width:976px}
.commit .panel{top:0;height:346px;background:var(--mist)}
.list-title{font-family:"Ubuntu",sans-serif;font-size:25px;font-weight:500;color:var(--sky)}
.ticks{list-style:none;margin-top:24px}
.ticks li{display:flex;align-items:center;font-size:14px;line-height:30px}
.ticks svg{width:14px;height:14px;margin-right:13px;fill:none;stroke:var(--sky);stroke-width:1.6}
.commit .text{position:absolute;left:40px;top:66px}
.frame{position:absolute;background:#fff}
.photo-portrait-m{background:linear-gradient(160deg,#c9d6de,#6e7f8c 50%,#2f3b46)}
.photo-portrait-f{background:linear-gradient(160deg,#9aa4a6,#cfc3b6 45%,#6b3a3a)}

/* sectors */
.sectors{position:relative;height:451px}
.sectors .panel{top:0;height:374px;background:#d3eef9}
.sectors .text{position:absolute;left:588px;top:64px}

/* cta */
.cta{height:268px;background:linear-gradient(90deg,#0a8ccf,#0ba4dc 60%,#0b8fd0);color:#fff;text-align:center;padding-top:30px}
.cta h2{font-family:"Ubuntu",sans-serif;font-size:34px;font-weight:500;line-height:48px}
.cta p{font-size:14px;line-height:26px}
.cta .lead{margin-top:20px}
.cta .btn-ghost{margin-top:24px;padding:0 31px}

/* footer */
.site-footer{height:223px;background:var(--dark);color:#fff;text-align:center;padding-top:58px}
.site-footer .brand{font-size:25px}
.site-footer .nav{height:auto;margin-top:22px;border-bottom:1px solid #3a3a3c;padding-bottom:14px}
.site-footer .bottom{display:flex;justify-content:space-between;align-items:center;font-size:13px;color:#d0d0d0;margin-top:10px}
.social{display:flex;gap:10px}
.social span{width:14px;height:14px;border-radius:50%;background:#fff;display:block}
</style>
</head>
<body>

<header class="site-header">
  <div class="wrap">
    <div class="top">
      <a class="brand" href="#">DROVE EXECUTIVE SEARCH</a>
      <a class="btn-solid" href="#">Get in touch</a>
    </div>
    <nav class="nav">
      <a href="#">About</a><a href="#">Services</a><a href="#">Industry Coverage</a><a href="#">Recruiting Process</a><a href="#">Retained Agreement</a><a href="#">Personal Commitment</a><a href="#">Testimonials</a><a href="#">Blogs</a><a href="#">Contact</a>
    </nav>
  </div>
</header>

<section class="hero" role="img" aria-label="Glass office building facade in blue tones">
  <div class="inner"></div>
  <div class="welcome">Welcome to</div>
  <h1>DROVE EXECUTIVE SEARCH</h1>
  <a class="btn-ghost" href="#">Get in touch</a>
</section>

<section class="about">
  <div class="wrap">
    <div class="about-title">
      <div class="kicker">ABOUT</div>
      <div class="big">DROVE EXECUTIVE<br>SEARCH</div>
    </div>
    <div class="about-text">
      <p>Welcome to the Harbor &amp; Quillstone recruiting website! If you are looking to grow your team or change careers, you’re at the right place. I’m Colette, the Founder and President of H&amp;Q, dedicated to matching job openings with job seekers.</p>
      <p>My passion for recruiting developed out of my desire to help people change their lives. During my 30+ year business career, I experienced downsizings, relocation, and offshoring. As a result, I developed a thick skin and an empathetic soul. These personal experiences, support my ability to connect with people who trust my judgement and integrity.</p>
      <p>As a recruiter, I know the importance of matching the right job requirements with the right individuals. I am tenacious, persuasive, and persistent and the recruiter you want to represent your company or, you the candidate.</p>
    </div>
  </div>
</section>

<section class="audience">
  <div class="wrap">
    <div class="col">
      <h2>FOR CLIENTS</h2>
      <p>If you are a company and looking to grow or change your team, join the clients who have relied on me for their most senior and critical placements.</p>
      <p>My client relationships start with understanding your corporate culture, your business needs and speaking with members of your HR team, the hiring manager, and the prospective new-hire’s peers. Capturing information through in-depth conversations, enables me to analyze and create a customized and tailored search to fill your open positions.</p>
    </div>
    <div class="col">
      <h2>FOR CANDIDATES</h2>
      <p>You are critical to the recruiting process. The former candidates I’ve worked with find me refreshingly honest, responsive, and trustworthy. My goals are to understand you, your needs, and skills as they relate to the position you are exploring. What is most important to you in a new position? Is it personal/career growth, financial, creativity, job flexibility, etc.? If the fit is there, we will highlight the best parts of you in your resume and promote you as a viable candidate for the role. Honesty and clarity are important in how you present yourself and how well your resume reflects what you do now, and what you can do in your next career move.</p>
    </div>
  </div>
</section>

<section class="more">
  <h2 class="section-title">A LITTLE MORE ABOUT ME</h2>
  <div class="wrap cols">
    <div class="col">
      <p>Most recently, I was a retained recruiter for a $1.5B digital transformation co. In the last two years alone, I used my “personal approach,” to place nearly 20 of their new Directors, VPs, SVPs and contributed to C-Suites search efforts.</p>
      <p>Earlier in my career, I built global business teams for Kestrel Banking Group, Ardent Advisory and Lindqvist Data and was part of the Meridian Wire sales team. I’ve interviewed 1000s of professionals; hired and fired countless others; and managed global teams both onsite and offshore.</p>
    </div>
    <div class="col">
      <p>I have an extensive research background which fuels my creative sourcing skills as I seek to find the “needle in the haystack” passive candidate who is not looking for a new role. I get tremendous pleasure presenting a compelling new career opportunity to a passive candidate, and watch them become a prospective candidate. And when my client wants to schedule an interview – the magic begins!</p>
      <p class="accent">As a solo practitioner, I am responsible for both clients and candidates. I will work tirelessly to find the match between job specs and job seekers.</p>
      <p>Let’s discuss how we can work together to find the ideal fit for your company or for you, as a candidate.</p>
      <p class="accent">How can I help you ?</p>
    </div>
  </div>
  <div class="photo photo-meeting" role="img" aria-label="Two professionals talking in a modern lounge"></div>
  <div class="photo photo-team" role="img" aria-label="Business team shaking hands and applauding in an office"></div>
</section>

<section class="process">
  <h2 class="section-title">RECRUITING PROCESS</h2>
  <div class="sub">The retainer agreement outlines the process:</div>

  <svg width="1200" height="724" style="position:absolute;left:0;top:0" aria-hidden="true">
    <polyline points="80,262 80,295 128,295 205,372 317,295 394,372 504,295 583,372 699,295 777,372 886,295 963,372 1073,295 1073,262" fill="none" stroke="#c3c3c3" stroke-width="18" stroke-linejoin="round"/>
  </svg>

  <div class="step" style="left:44px;bottom:512px"><div class="num">01</div>Candidate Consult &amp;<br>Advisement</div>
  <div class="step" style="left:233px;bottom:512px"><div class="num">03</div>Candidate List<br>Generation</div>
  <div class="step" style="left:419px;bottom:512px"><div class="num">05</div>Candidate Outreach<br>/Pre-Qualifying Interviews<br>/Documentation</div>
  <div class="step" style="left:615px;bottom:512px"><div class="num">07</div>Candidate Response<br>Review</div>
  <div class="step" style="left:801px;bottom:536px"><div class="num">09</div>Interview Prep</div>
  <div class="step" style="left:988px;bottom:536px"><div class="num">11</div>Offer Presentation</div>

  <div class="tile" style="left:87px;top:232px"><svg viewBox="0 0 24 24"><path d="M9 18h6M10 21h4M12 3a6 6 0 0 0-3.5 10.9V16h7v-2.1A6 6 0 0 0 12 3z"/></svg></div>
  <div class="tile" style="left:276px;top:232px"><svg viewBox="0 0 24 24"><rect x="5" y="4" width="14" height="17" rx="1"/><path d="M9 3h6v3H9zM8 10h8M8 14h8M8 18h5"/></svg></div>
  <div class="tile" style="left:463px;top:232px"><svg viewBox="0 0 24 24"><path d="M4 14l10-8 4 4-8 10zM14 6l3-3 4 4-3 3M6 16l2 2"/></svg></div>
  <div class="tile" style="left:658px;top:232px"><svg viewBox="0 0 24 24"><rect x="3" y="6" width="18" height="12" rx="1"/><path d="M7 12h0M12 12h0M17 12h0"/></svg></div>
  <div class="tile" style="left:845px;top:232px"><svg viewBox="0 0 24 24"><rect x="4" y="3" width="14" height="18" rx="1"/><circle cx="11" cy="10" r="3"/><path d="M7 18h8M20 8v12"/></svg></div>
  <div class="tile" style="left:1032px;top:232px"><svg viewBox="0 0 24 24"><rect x="4" y="3" width="16" height="18" rx="1"/><circle cx="12" cy="10" r="3"/><path d="M7 18c1-3 9-3 10 0"/></svg></div>

  <div class="tile" style="left:164px;top:337px"><svg viewBox="0 0 24 24"><path d="M3 8l6-3 6 3 6-3v11l-6 3-6-3-6 3zM9 5v11M15 8v11"/></svg></div>
  <div class="tile" style="left:353px;top:337px"><svg viewBox="0 0 24 24"><circle cx="12" cy="8" r="3"/><circle cx="6" cy="10" r="2"/><circle cx="18" cy="10" r="2"/><path d="M7 19c0-4 10-4 10 0M2 18c0-3 5-3 5-3M22 18c0-3-5-3-5-3"/></svg></div>
  <div class="tile" style="left:542px;top:337px"><svg viewBox="0 0 24 24"><circle cx="11" cy="7" r="4"/><path d="M11 11v8l3-2 3 3"/></svg></div>
  <div class="tile" style="left:736px;top:337px"><svg viewBox="0 0 24 24"><circle cx="14" cy="10" r="6"/><path d="M9 14l-5 5M12 10h4"/></svg></div>
  <div class="tile" style="left:922px;top:337px"><svg viewBox="0 0 24 24"><rect x="4" y="5" width="16" height="12" rx="1"/><path d="M8 9h8M8 13h5M8 17l-2 3"/></svg></div>

  <div class="step" style="left:120px;top:428px">Sourcing<div class="num">02</div></div>
  <div class="step" style="left:309px;top:428px">Internal Team<br>Review<div class="num">04</div></div>
  <div class="step" style="left:498px;top:428px">Present Candidates /<br>Internal Assessment<div class="num">06</div></div>
  <div class="step" style="left:692px;top:428px">Interview<br>Management<div class="num">08</div></div>
  <div class="step" style="left:878px;top:428px">Post-Interview Feedback<div class="num" style="margin-top:24px">10</div></div>

  <p class="note">A correct placement takes time and attention. I am committed to finding the best executive, with the right skills you need, out of the gate, but want you to understand finding the best candidate may take longer than expected. Rest assured, I will put in the time it takes and will be with you through the entire process: your satisfaction is my success.</p>
</section>

<section class="commit">
  <div class="panel">
    <div class="text">
      <h3 class="list-title">MY PERSONAL COMMITMENT</h3>
      <ul class="ticks">
        <li><svg viewBox="0 0 14 14"><circle cx="7" cy="7" r="6"/><path d="M4 7l2 2 4-4"/></svg>Dedicated service</li>
        <li><svg viewBox="0 0 14 14"><circle cx="7" cy="7" r="6"/><path d="M4 7l2 2 4-4"/></svg>Customer satisfaction</li>
        <li><svg viewBox="0 0 14 14"><circle cx="7" cy="7" r="6"/><path d="M4 7l2 2 4-4"/></svg>Develop and maintain trust</li>
        <li><svg viewBox="0 0 14 14"><circle cx="7" cy="7" r="6"/><path d="M4 7l2 2 4-4"/></svg>Adherance to strict confidentiality</li>
        <li><svg viewBox="0 0 14 14"><circle cx="7" cy="7" r="6"/><path d="M4 7l2 2 4-4"/></svg>Provide detailed feedback</li>
      </ul>
    </div>
  </div>
  <div class="frame" style="left:694px;top:28px;width:394px;height:318px"></div>
  <div class="frame photo-portrait-m" style="left:710px;top:45px;width:336px;height:347px" role="img" aria-label="Smiling businessman at a desk in front of a whiteboard"></div>
</section>

<section class="sectors">
  <div class="panel"></div>
  <div class="frame" style="left:170px;top:47px;width:335px;height:327px"></div>
  <div class="frame photo-portrait-f" style="left:154px;top:63px;width:311px;height:346px" role="img" aria-label="Smiling woman holding a tablet"></div>
  <div class="text">
    <h3 class="list-title">SECTOR SPECIALTIES</h3>
    <ul class="ticks">
      <li><svg viewBox="0 0 14 14"><circle cx="7" cy="7" r="6"/><path d="M4 7l2 2 4-4"/></svg>Finance</li>
      <li><svg viewBox="0 0 14 14"><circle cx="7" cy="7" r="6"/><path d="M4 7l2 2 4-4"/></svg>Human Resources</li>
      <li><svg viewBox="0 0 14 14"><circle cx="7" cy="7" r="6"/><path d="M4 7l2 2 4-4"/></svg>Sales and Marketing</li>
      <li><svg viewBox="0 0 14 14"><circle cx="7" cy="7" r="6"/><path d="M4 7l2 2 4-4"/></svg>Innovation and Transformation</li>
      <li><svg viewBox="0 0 14 14"><circle cx="7" cy="7" r="6"/><path d="M4 7l2 2 4-4"/></svg>Information Technology</li>
      <li><svg viewBox="0 0 14 14"><circle cx="7" cy="7" r="6"/><path d="M4 7l2 2 4-4"/></svg>Entertainment/Media/Technology</li>
      <li><svg viewBox="0 0 14 14"><circle cx="7" cy="7" r="6"/><path d="M4 7l2 2 4-4"/></svg>Healthcare/Life Sciences/HCIT/Biotechnology</li>
    </ul>
  </div>
</section>

<section class="cta">
  <h2>HOW CAN I HELP YOU?</h2>
  <p class="lead">Contact H&amp;Q to learn more about the recruiting services or to answer your questions.</p>
  <p>CONNECTING TALENTED PEOPLE WITH DYNAMIC OPPORTUNITIES AT EXCELENT COMPANIES</p>
  <a class="btn-ghost" href="#">Calendar Sign Up</a>
</section>

<footer class="site-footer">
  <div class="wrap">
    <div class="brand">DROVE EXECUTIVE SEARCH</div>
    <nav class="nav">
      <a href="#">About</a><a href="#">Services</a><a href="#">Industry Coverage</a><a href="#">Recruiting Process</a><a href="#">Retained Agreement</a><a href="#">Personal Commitment</a><a href="#">Testimonials</a><a href="#">Blogs</a><a href="#">Contact</a>
    </nav>
    <div class="bottom">
      <span>2023 Drove Executive Search. All Rights Reserved.</span>
      <div class="social" aria-label="Social links"><span></span><span></span><span></span></div>
    </div>
  </div>
</footer>

</body>
</html>
```